Innovative Healthcare Technology Company needs a Business Card Design

We are in need of an innovative business card design for a new healthcare software company called "Lumenwise Data Partners". We develop software that creates medical assessment applications and mobile e-learning prevention services to reduce risk behaviors in adolescent and young adults. Our initial product, the "KESTREL App", conducts a tailored sexual risk assessment and provides a doctor with an insightful patient report to improve sexual risk counseling and ultimately reduce unintended pregnancy, STDs, etc.

We would like the design to incorporate our logo and branding colors (attached) in an innovative and creative manner. The final design should communicate professionalism and healthcare innovation. Our tag line is "prevention is the solution" (doesn't necessarily need to be included) and our target audience is doctors, medical directors, and medical business administrators. Please visit our website for additional info ourbrightmarq.com. Be creative and we look forward to seeing your designs!

Target Market(s)

healthcare - doctors, medical directors and medical business administrators

Industry/Entity Type

Healthcare

Contact Information for Business Card

We would like the design to incorporate our logo and branding colors (attached) in an innovative and creative manner. The final design should communicate professionalism and healthcare innovation. Our tag line is "prevention is the solution" (doesn't necessarily need to be included)

Font styles to use
Other font styles liked:
• quicksand

Requirements
Must have
• our logo and brand colors
• Name, (Mara Feldhovenik, PhD)
• Email (drmara@ourbrightmarq.com)
• phone (555.283.9170)
• Website (ourbrightmarq.com)
Should not have
• cartoon look

```html
<!DOCTYPE html>
<html lang="en">
<head>
<meta charset="utf-8">
<title>Lumenwise Data Partners – Business Card</title>
<link href="https://fonts.googleapis.com/css2?family=Quicksand:wght@400;500;600&display=swap" rel="stylesheet">
<style>
  :root {
    --stage: #4a4a4a;
    --card-white: #ffffff;
    --card-black: #151618;
    --brand-blue: #1b4f9c;
    --brand-blue-light: #3f7fbf;
    --brand-green: #6fb49a;
    --text-light: #ffffff;
  }
  * { margin: 0; padding: 0; box-sizing: border-box; }
  html, body {
    width: 1200px; height: 900px; overflow: hidden;
    background: var(--stage);
    font-family: "Quicksand", sans-serif;
  }
  .canvas {
    position: relative; width: 1200px; height: 900px;
    display: flex; flex-direction: column; align-items: center; justify-content: center; gap: 40px;
  }
  .card {
    position: relative; width: 660px; height: 377px;
    border-radius: 28px; overflow: hidden;
  }
  .card--back { background: var(--card-black); }
  .card--front { background: var(--card-white); }

  .brand { position: absolute; display: flex; align-items: center; gap: 16px; }
  .brand__mark { width: 34px; height: 34px; background: var(--brand-blue); flex: none; }
  .brand__name {
    font-weight: 500; color: var(--brand-blue); line-height: 1.05;
    font-size: 36px; letter-spacing: 1px; white-space: nowrap;
  }
  .card--back .brand { left: 50%; top: 50%; transform: translate(-50%, -50%); }
  .card--front .brand { left: 92px; top: 36px; }

  .wave { position: absolute; inset: 0; width: 100%; height: 100%; }

  .holder {
    position: absolute; left: 44px; top: 248px;
    color: var(--text-light); font-size: 22px; font-weight: 500; letter-spacing: 0.5px;
    white-space: nowrap;
  }
  .contact {
    position: absolute; left: 366px; top: 160px; list-style: none;
    color: var(--text-light); font-size: 17px; font-weight: 500; letter-spacing: 0.2px;
    white-space: nowrap;
  }
  .contact__item { display: flex; align-items: center; gap: 10px; height: 28px; }
  .contact__icon { width: 20px; height: 16px; flex: none; }
</style>
</head>
<body>
<main class="canvas">
  <section class="card card--back" aria-label="Business card, back">
    <div class="brand">
      <span class="brand__mark"></span>
      <span class="brand__name">Lumenwise<br>Data Partners</span>
    </div>
  </section>

  <section class="card card--front" aria-label="Business card, front">
    <svg class="wave" viewBox="0 0 660 377" preserveAspectRatio="none" aria-hidden="true">
      <defs>
        <linearGradient id="bandGradient" x1="0" y1="0" x2="1" y2="0">
          <stop offset="0" stop-color="#1b4f9c"/>
          <stop offset="1" stop-color="#3f7fbf"/>
        </linearGradient>
      </defs>
      <path d="M0 192 C 220 186, 440 150, 660 108 L 660 232 C 440 266, 220 304, 0 352 Z" fill="url(#bandGradient)"/>
      <path d="M0 352 C 220 304, 440 266, 660 232 L 660 242 C 440 276, 220 314, 0 362 Z" fill="#6fb49a"/>
    </svg>

    <div class="brand">
      <span class="brand__mark"></span>
      <span class="brand__name">Lumenwise<br>Data Partners</span>
    </div>

    <p class="holder">Mara Feldhovenik, PhD</p>

    <ul class="contact">
      <li class="contact__item">
        <svg class="contact__icon" viewBox="0 0 20 16" aria-hidden="true"><rect x="1" y="2" width="18" height="12" fill="none" stroke="#fff" stroke-width="1.6"/><path d="M1 2 L10 9 L19 2" fill="none" stroke="#fff" stroke-width="1.6"/></svg>
        drmara@ourbrightmarq.com
      </li>
      <li class="contact__item">
        <svg class="contact__icon" viewBox="0 0 20 16" aria-hidden="true"><path d="M1 5 Q10 -1 19 5 L17 7 L14 5 L6 5 L3 7 Z" fill="#fff"/><rect x="4" y="8" width="12" height="7" rx="1" fill="#fff"/></svg>
        555.283.9170
      </li>
      <li class="contact__item">
        <svg class="contact__icon" viewBox="0 0 20 16" aria-hidden="true"><g fill="none" stroke="#fff" stroke-width="1.3"><circle cx="10" cy="8" r="7"/><ellipse cx="10" cy="8" rx="3" ry="7"/><path d="M3 8 H17 M4.5 4 H15.5 M4.5 12 H15.5"/></g></svg>
        ourbrightmarq.com
      </li>
    </ul>
  </section>
</main>
</body>
</html>
```